Copperleaf Vantage Training PowerPoint Template

I want to PowerPoint template theme using my attached logo. My colors are black and orange. My website is CopperleafVantage.com. I am a handgun training company.

Font:

- Serpentine-Bold-Bold for "IRON BRAE"

- BrowalliaUPC for "SHOOTING SPORTS"

Colors (CMYK code):

- BLACK ....... 0; 0; 0; 100;
- ORANGE ... gradient from 0; 65; 97.5; 0 to 0; 39; 97.5; 0

```html
<!DOCTYPE html>
<html lang="en">
<head>
<meta charset="utf-8">
<title>Copperleaf Vantage Training – Cover Slide</title>
<link rel="stylesheet" href="https://fonts.googleapis.com/css2?family=Carlito:wght@400;700&display=swap">
<style>
  :root {
    --black: #000000;
    --orange-deep: #f0790a;
    --orange-light: #f8a81a;
    --title-orange: #f08a00;
    --text-grey: #7a7a7a;
    --frame-grey: #6e6e6e;
    --steel: #4a4a4a;
    --gold: #f5c242;
    --white: #ffffff;
  }
  html, body {
    margin: 0;
    padding: 0;
    overflow: hidden;
    background: var(--white);
  }
  .slide {
    position: relative;
    width: 1200px;
    height: 676px;
    overflow: hidden;
    background: var(--white);
    font-family: "Carlito", "Calibri", sans-serif;
  }
  .brand {
    position: absolute;
    left: 69px;
    top: 92px;
    display: flex;
    align-items: center;
    gap: 14px;
  }
  .brand-mark {
    width: 44px;
    height: 44px;
    background: var(--orange-deep);
  }
  .brand-name {
    font-weight: 700;
    font-size: 26px;
    line-height: 1;
    color: var(--black);
  }
  .title-frame {
    position: absolute;
    left: 67px;
    top: 252px;
    width: 986px;
    height: 99px;
    box-sizing: border-box;
    border: 1px dashed var(--frame-grey);
  }
  .slide-title {
    position: absolute;
    left: 9px;
    top: 26px;
    margin: 0;
    font-weight: 400;
    font-size: 52px;
    line-height: 1;
    color: var(--title-orange);
  }
  .subhead {
    position: absolute;
    left: 76px;
    top: 356px;
    margin: 0;
    font-size: 19px;
    color: var(--text-grey);
  }
  .author-frame {
    position: absolute;
    left: 67px;
    top: 521px;
    width: 369px;
    height: 63px;
    box-sizing: border-box;
    border: 1px dashed var(--frame-grey);
  }
  .author {
    position: absolute;
    left: 8px;
    top: 4px;
    margin: 0;
    font-size: 14px;
    color: var(--text-grey);
  }
  .footer-band {
    position: absolute;
    left: 0;
    bottom: 0;
    width: 1200px;
    height: 73px;
  }
</style>
</head>
<body>
  <main class="slide">
    <div class="brand">
      <div class="brand-mark"></div>
      <div class="brand-name">Copperleaf Vantage Training</div>
    </div>

    <div class="title-frame">
      <h1 class="slide-title">Cover page</h1>
    </div>
    <p class="subhead">Subhead</p>

    <div class="author-frame">
      <p class="author">Author</p>
    </div>

    <svg class="footer-band" viewBox="0 0 1200 73" aria-hidden="true">
      <defs>
        <linearGradient id="accent-line" x1="0" x2="1" y1="0" y2="0">
          <stop offset="0" stop-color="var(--steel)"/>
          <stop offset="0.55" stop-color="#8a7a55"/>
          <stop offset="0.82" stop-color="var(--gold)"/>
          <stop offset="1" stop-color="var(--steel)"/>
        </linearGradient>
        <linearGradient id="orange-band" x1="0" x2="1" y1="0" y2="0">
          <stop offset="0" stop-color="var(--orange-deep)"/>
          <stop offset="0.8" stop-color="var(--orange-light)"/>
          <stop offset="1" stop-color="var(--orange-deep)"/>
        </linearGradient>
      </defs>
      <rect x="0" y="0" width="1200" height="6" fill="url(#accent-line)"/>
      <rect x="0" y="6" width="1200" height="11" fill="url(#orange-band)"/>
      <rect x="0" y="17" width="1200" height="56" fill="var(--black)"/>
    </svg>
  </main>
</body>
</html>
```